One page website for a Personal Injury Law Firm

Design and code a one page website in WordPress for the Darrow Law Firm, which is a a personal injury law firm located in Coral Gables, Florida. Please note: if you want to change the color pallete for the logo and for the web design , that is fine by me.

Target Market(s)

Those injured in accidents that need legal representation

Industry/Entity Type

Legal

Coding

Coded - Design and coding required

Number of Pages Required

1 page

Font styles to use
Other font styles liked:
• Montserrat

```html
<!DOCTYPE html>
<html lang="en">
<head>
<meta charset="utf-8">
<title>Darrow Law Firm – Personal Injury Representation</title>
<link href="https://fonts.googleapis.com/css2?family=Montserrat:wght@400;500;600;700;800&display=swap" rel="stylesheet">
<style>
:root{
  --gold:#c4935c;
  --gold-dark:#a97a46;
  --ink:#1f1f1f;
  --text:#3a3a3a;
  --muted:#6b6b6b;
  --light:#ececec;
  --dark:#2e2e2e;
  --footer:#232323;
  --white:#ffffff;
}
*{box-sizing:border-box;margin:0;padding:0}
html,body{width:1200px;height:5282px;overflow:hidden}
body{font-family:"Montserrat",sans-serif;color:var(--text);background:var(--white);position:relative}
section,header,footer{position:absolute;left:0;width:1200px}
.abs{position:absolute}
.label{font-size:13px;font-weight:600;color:var(--gold);letter-spacing:.5px;text-transform:uppercase}
.h2{font-size:30px;font-weight:700;color:var(--ink);letter-spacing:.5px;text-transform:uppercase}
.center{text-align:center;left:0;width:1200px}
.rule{height:3px;width:56px;background:var(--gold)}
.circle{border-radius:50%;background:var(--gold);display:flex;align-items:center;justify-content:center}
.hex{width:70px;height:76px;clip-path:polygon(50% 0,100% 25%,100% 75%,50% 100%,0 75%,0 25%);background:var(--gold);display:flex;align-items:center;justify-content:center}

/* header */
.site-header{top:0;height:123px;background:var(--white)}
.contact-mini{display:flex;align-items:center;gap:10px;font-size:13px;color:var(--ink)}
.contact-mini b{display:block;color:var(--gold);font-weight:700;font-size:13px}
.nav a{font-size:13.5px;color:var(--ink);text-decoration:none;margin-right:34px}
.nav a.active{color:var(--gold);border-bottom:2px solid var(--gold);padding-bottom:3px}
.logo-tab{left:500px;top:0;width:200px;height:142px;background:var(--white);border-radius:0 0 30px 30px;text-align:center;z-index:3}
.brand{font-size:34px;font-weight:600;color:var(--ink);letter-spacing:.5px}
.brand-sub{font-size:11px;font-weight:600;color:var(--ink);letter-spacing:4px}
.social{width:34px;height:34px}
.btn-gold{background:var(--gold);color:var(--white);font-weight:700;font-size:14px;text-transform:uppercase;display:flex;align-items:center;justify-content:center;box-shadow:0 0 0 3px var(--white),0 0 0 4px var(--gold)}

/* hero */
.hero{top:123px;height:609px;background:linear-gradient(90deg,#f1f1f1 0%,#d9d9d9 40%,#b9b9b9 70%,#e3e3e3 100%);overflow:hidden}
.hero-photo{right:0;top:0;width:700px;height:609px;background:linear-gradient(180deg,#cfcfcf,#9a9a9a 60%,#5d6273)}
.hero-title{left:111px;top:188px;font-size:31px;font-weight:600;color:var(--ink);line-height:43px;text-transform:uppercase}
.hero-title span{color:var(--gold);font-size:37px;font-weight:700}
.btn-outline{border:2px solid var(--gold);color:var(--gold-dark);font-size:14px;font-weight:700;display:flex;align-items:center;justify-content:center;background:rgba(255,255,255,.4);box-shadow:inset 0 0 0 3px var(--white),inset 0 0 0 5px var(--gold)}

/* about */
.about{top:732px;height:881px;background:var(--white)}
.about-frame{left:175px;top:230px;width:440px;height:320px;background:var(--gold);border-radius:0 60px 0 0}
.about-photo{left:162px;top:234px;width:440px;height:381px;background:linear-gradient(135deg,#5a4030,#2a2220 60%,#7a6048)}
.feature{left:642px;width:460px;display:flex;gap:24px}
.feature .hex{flex:none}
.feature h4{font-size:14.5px;font-weight:600;color:var(--gold);margin-bottom:4px}
.feature p{font-size:13.5px;line-height:21px;color:var(--text)}
.about-copy{left:162px;top:662px;width:915px;font-size:14px;line-height:25px;color:var(--text)}
.about-copy p+p{margin-top:14px}

/* practice */
.practice{top:1613px;height:833px;background:var(--light)}
.cards{left:111px;top:263px;width:980px;display:grid;grid-template-columns:repeat(4,229px);column-gap:21px;row-gap:21px}
.card{height:216px;background:var(--white);border:1px solid #d8d8d8;text-align:center;padding:22px 18px 0}
.card.dark{background:var(--dark);border:5px solid var(--gold);box-shadow:0 0 0 2px #cfcfcf}
.card .ico{width:60px;height:42px;margin:0 auto 8px;border-radius:6px;background:linear-gradient(135deg,#e6c9a4,#c4935c)}
.card h3{font-size:15px;font-weight:600;color:var(--ink);line-height:22px;margin-bottom:10px}
.card.dark h3,.card.dark p{color:var(--white)}
.card p{font-size:11px;line-height:18px;color:var(--muted)}

/* contact band */
.contact-band{top:2446px;height:498px;background:var(--dark)}
.contact-band .h2{color:var(--white)}
.band-copy{left:130px;top:176px;width:940px;text-align:center;color:#e4e4e4;font-size:13.5px;line-height:25px}
.band-copy p+p{margin-top:8px}
.pill{display:flex;align-items:center;border:2px solid var(--gold);height:52px;color:var(--white);font-size:14px}
.pill .sq{width:58px;height:48px;background:var(--gold);display:flex;align-items:center;justify-content:center;margin-right:22px;flex:none}
.pill b{display:block;font-size:12px;font-weight:700;text-transform:uppercase}

/* strategy */
.strategy{top:2944px;height:525px;background:var(--white)}
.s-card{background:#ebebeb;border-radius:22px;text-align:center;padding:0 32px}
.s-card.dark{background:var(--footer);color:var(--white)}
.s-card h3{font-size:17px;font-weight:600;color:var(--ink);margin-bottom:12px}
.s-card.dark h3{color:var(--white)}
.s-card p{font-size:13px;line-height:22px;color:var(--muted)}
.s-card.dark p{color:#e2e2e2}
.s-hex{left:50%;transform:translateX(-50%)}

/* know */
.know{top:3469px;height:750px;background:linear-gradient(180deg,#f4f4f4,#dedede 50%,#ececec)}
.know-photo{left:595px;top:254px;width:434px;height:387px;background:linear-gradient(135deg,#8a8f9e,#3f4a66 50%,#5e4a3c)}
.know-card{left:158px;top:297px;width:490px;height:303px;background:var(--white);padding:54px 56px;box-shadow:0 6px 24px rgba(0,0,0,.08)}
.know-card h3{font-size:20px;font-weight:600;color:var(--ink);line-height:28px}
.know-card h3 span{color:var(--gold)}
.know-card p{font-size:14px;line-height:25px;margin-top:14px}
.arrow{width:34px;height:30px;display:inline-flex;align-items:center;justify-content:center;margin-right:6px}

/* promise */
.promise{top:4219px;height:340px;background:var(--gold)}
.promise .label{color:var(--white)}
.promise .h2{color:#f6eadb}
.promise-item{top:162px;display:flex;align-items:center;gap:22px;color:var(--white);font-size:21px;line-height:26px;letter-spacing:.5px}
.hex-o{width:80px;height:88px;flex:none}

/* cta */
.cta{top:4559px;height:419px;background:linear-gradient(90deg,#eeeeee 0%,#fafafa 45%,#ffffff 100%)}
.cta-photo{left:140px;top:0;width:393px;height:419px;background:linear-gradient(180deg,#d6d6d6,#4a5064 70%,#2c3044)}
.cta h2{font-size:31px;font-weight:700;color:var(--ink);line-height:42px;text-transform:uppercase}
.pill.light{color:var(--ink)}
.pill.light b{color:var(--gold)}

/* footer */
.site-footer{top:4978px;height:304px;background:var(--footer);color:var(--white)}
.foot-nav{top:66px;width:1200px;text-align:center;font-size:12px}
.foot-nav a{color:var(--white);text-decoration:none;margin:0 10px}
.foot-nav span{color:#888}
.foot-col{top:144px;display:flex;gap:20px;font-size:13px;line-height:22px}
.foot-col b{display:block;font-size:12.5px;font-weight:700}
.copy{left:396px;top:262px;font-size:12.5px;color:#dcdcdc}
</style>
</head>
<body>

<header class="site-header">
  <div class="abs contact-mini" style="left:111px;top:20px">
    <div class="circle" style="width:34px;height:34px">
      <svg width="16" height="16" viewBox="0 0 24 24" fill="#fff"><path d="M6.6 10.8a15 15 0 006.6 6.6l2.2-2.2c.3-.3.7-.4 1-.2 1.1.4 2.3.6 3.6.6.6 0 1 .4 1 1V20c0 .6-.4 1-1 1A17 17 0 013 4c0-.6.4-1 1-1h3.5c.6 0 1 .4 1 1 0 1.3.2 2.5.6 3.6.1.3 0 .7-.2 1z"/></svg>
    </div>
    <div><b>CALL US :</b>(305) 555-0182</div>
  </div>
  <div class="abs contact-mini" style="left:307px;top:20px">
    <div class="circle" style="width:34px;height:34px">
      <svg width="16" height="16" viewBox="0 0 24 24" fill="#fff"><path d="M3 5h18v14H3z" opacity=".0"/><path d="M2 5h20v14H2V5zm2 2v.5l8 5 8-5V7H4z"/></svg>
    </div>
    <div><b>CALL US :</b>info@darrowlegal-example.com</div>
  </div>
  <nav class="abs nav" style="left:111px;top:80px">
    <a class="active">Home</a><a>About Us</a><a>Why Choose The Darrow</a>
  </nav>
  <div class="abs logo-tab">
    <div style="width:50px;height:50px;border:2px solid var(--ink);margin:20px auto 6px"></div>
    <div class="brand">Darrow</div>
    <div class="brand-sub">LAW FIRM</div>
  </div>
  <div class="abs" style="left:701px;top:28px;font-size:13px;color:var(--ink)">Follow Us :</div>
  <div class="abs circle social" style="left:790px;top:20px"></div>
  <div class="abs circle social" style="left:831px;top:20px"></div>
  <div class="abs circle social" style="left:872px;top:20px"></div>
  <div class="abs btn-gold" style="left:951px;top:18px;width:132px;height:38px">Contact Us</div>
  <nav class="abs nav" style="left:707px;top:80px">
    <a>Our Strategy</a><a>Practice Areas</a><a style="margin-right:0">What You Need to Know</a>
  </nav>
</header>

<section class="hero">
  <div class="abs hero-photo" role="img" aria-label="Waterfront city skyline with an attorney in a suit, arms crossed"></div>
  <h1 class="abs hero-title"><span>CONCIERGE-LEVEL</span><br>Personal Injury<br>Representation in Miami,<br>Florida</h1>
  <div class="abs btn-outline" style="left:115px;top:390px;width:204px;height:50px">FREE CONSULTATION</div>
</section>

<section class="about">
  <div class="abs label center" style="top:84px">About Us</div>
  <h2 class="abs h2 center" style="top:106px">Why Choose The Darrow Law Firm?</h2>
  <div class="abs rule" style="left:572px;top:160px"></div>
  <p class="abs center" style="top:178px;font-size:14px;color:var(--ink)">Unmatched Experience. Proven Results. Relentless Advocacy.</p>
  <div class="abs about-frame"></div>
  <div class="abs about-photo" role="img" aria-label="Attorney in a suit addressing a courtroom"></div>

  <div class="abs feature" style="top:244px">
    <div class="hex"><svg width="34" height="34" viewBox="0 0 24 24" fill="none" stroke="#fff" stroke-width="1.6"><path d="M12 3v18M5 21h14M4 7h16M7 7l-3 7h6zM17 7l-3 7h6z"/></svg></div>
    <div><h4>25+ Years of Legal Mastery :</h4><p>We have successfully handled thousands of cases, fighting both for and against insurance companies. This unique dual experience gives us an insider advantage in every case we take on.</p></div>
  </div>
  <div class="abs feature" style="top:366px">
    <div class="hex"><svg width="30" height="30" viewBox="0 0 24 24" fill="none" stroke="#fff" stroke-width="1.6"><path d="M6 21h12M8 21V9h8v12M7 9V4h2v2h2V4h2v2h2V4h2v5"/></svg></div>
    <div><h4>Extensive Knowledge of Insurance Tactics:</h4><p>Having worked for insurance companies, we know their strategies, loopholes, and how to dismantle their defenses to maximize your settlement.</p></div>
  </div>
  <div class="abs feature" style="top:480px">
    <div class="hex"><svg width="34" height="30" viewBox="0 0 24 24" fill="#fff"><circle cx="12" cy="7" r="3"/><circle cx="5" cy="9" r="2.2"/><circle cx="19" cy="9" r="2.2"/><path d="M7 20v-4a5 5 0 0110 0v4zM1 19v-3a4 4 0 015-3.6V19zM23 19v-3a4 4 0 00-5-3.6V19z"/></svg></div>
    <div><h4>Millions Recovered for Clients:</h4><p>Our track record includes life-changing results. A client fell eight feet at a major sporting venue and suffered catastrophic injuries. We recovered compensation that covered all medical bills, paid off their home, and funded their children’s college education.</p></div>
  </div>

  <div class="abs about-copy">
    <p>A client suffered a severe infection from a minor slip-and-fall injury in a Miami condo building. We resolved the case before filing a lawsuit, securing funds that allowed him to buy a new home, pay off debts, and provide private school tuition for his children.</p>
    <p>A fast-food restaurant’s napkin dispenser fell on a customer’s face, breaking her nose and leaving her permanently disfigured. We secured a settlement that covered plastic surgery, home renovations, and her daughter’s college tuition. These are just a few examples of how we fight for our clients’ futures—not just their cases.</p>
  </div>
</section>

<section class="practice">
  <div class="abs label" style="left:111px;top:112px">What We Do</div>
  <h2 class="abs h2" style="left:111px;top:136px">Our Practice Areas</h2>
  <div class="abs rule" style="left:111px;top:186px;width:58px;height:2px"></div>
  <p class="abs" style="left:111px;top:202px;font-size:14px;color:var(--ink)">Comprehensive Representation for the Injured</p>
  <div class="abs cards">
    <div class="card"><div class="ico" role="img" aria-label="Car collision icon"></div><h3>Car Accidents</h3><p>We fight for victims of rear-end crashes, multi-vehicle collisions, pedestrian and cyclist accidents, and more.</p></div>
    <div class="card dark"><div class="ico" role="img" aria-label="Slip and fall icon"></div><h3>Slip and Fall</h3><p>If you were injured due to unsafe conditions at a business, hotel, condo, or public space, we hold negligent property owners accountable.</p></div>
    <div class="card"><div class="ico" role="img" aria-label="Wrongful death icon"></div><h3>Wrongful Death</h3><p>We provide compassionate yet fierce representation for families who have lost a loved one due to negligence.</p></div>
    <div class="card"><div class="ico" role="img" aria-label="Product liability icon"></div><h3>Product Liability</h3><p>We provide compassionate yet fierce representation for families who have lost a loved one due to negligence.</p></div>
    <div class="card"><div class="ico" role="img" aria-label="Truck accident icon"></div><h3>Truck and Commercial Vehicle Accidents</h3><p>Truck accidents often result in devastating injuries. We fight trucking companies and insurers to protect your rights.</p></div>
    <div class="card"><div class="ico" role="img" aria-label="Boating accident icon"></div><h3>Boating and Watercraft Accidents</h3><p>From reckless boaters to alcohol-related crashes, we hold negligent parties accountable.</p></div>
    <div class="card"><div class="ico" role="img" aria-label="Dog bite icon"></div><h3>Dog Bites and Animal Attacks</h3><p>Florida’s strict liability laws mean pet owners are responsible for injuries caused by their animals.</p></div>
    <div class="card"><div class="ico" role="img" aria-label="Workplace injury icon"></div><h3>Workplace Injuries (Third-Party Claims)</h3><p>If a third party’s negligence contributed to your workplace injury, a third party’s negligence contributed to your</p></div>
  </div>
</section>

<section class="contact-band">
  <div class="abs label center" style="top:90px">Contact Us</div>
  <h2 class="abs h2 center" style="top:114px;color:var(--white)">Justice. Recovery. A Better Future Starts Here.</h2>
  <div class="abs band-copy">
    <p>At The Darrow Law Firm, we understand that suffering a personal injury can be life-altering—physically, emotionally, and financially. You may be unsure whether pursuing legal action is the right step. But in Florida, holding negligent parties accountable isn’t just your right—it’s often necessary to rebuild your life.</p>
    <p>We take a concierge-style approach to personal injury law, offering personalized attention, strategic advocacy, and relentless dedication to securing the maximum compensation you deserve. Our mission is not only to make you whole again but to help you build a brighter future—ensuring access to the best medical care, financial stability, and peace of mind for you and your loved ones.</p>
  </div>
  <div class="abs pill" style="left:328px;top:358px;width:234px">
    <div class="sq"><svg width="22" height="22" viewBox="0 0 24 24" fill="#fff"><path d="M6.6 10.8a15 15 0 006.6 6.6l2.2-2.2c.3-.3.7-.4 1-.2 1.1.4 2.3.6 3.6.6.6 0 1 .4 1 1V20c0 .6-.4 1-1 1A17 17 0 013 4c0-.6.4-1 1-1h3.5c.6 0 1 .4 1 1 0 1.3.2 2.5.6 3.6.1.3 0 .7-.2 1z"/></svg></div>
    <div><b>Free Consultation :</b>(305) 555-0182</div>
  </div>
  <div class="abs pill" style="left:578px;top:358px;width:285px">
    <div class="sq"><svg width="22" height="22" viewBox="0 0 24 24" fill="#fff"><path d="M2 5h20v14H2V5zm2 2v.5l8 5 8-5V7H4z"/></svg></div>
    <div><b>Email:</b>info@darrowlegal-example.com</div>
  </div>
</section>

<section class="strategy">
  <div class="abs label center" style="top:88px">Our Strategy</div>
  <h2 class="abs h2 center" style="top:112px">Aggressive, Client-Focused, and Results-Driven</h2>

  <div class="abs s-card" style="left:92px;top:217px;width:332px;height:195px;padding-top:60px">
    <h3>Taking on Corporate Giants</h3>
    <p>We don’t back down from big insurance companies, property management firms, or major corporations. We fight for justice—no matter how powerful the opposition.</p>
  </div>
  <div class="abs s-card dark" style="left:433px;top:188px;width:332px;height:259px;padding-top:96px">
    <h3>Concierge-Style Legal Care</h3>
    <p>You’re not just another case number. We provide dedicated, personalized service, keeping you informed, supported, and empowered throughout the legal process.</p>
  </div>
  <div class="abs s-card" style="left:775px;top:217px;width:332px;height:195px;padding-top:60px">
    <h3>No Win, No Fee Guarantee</h3>
    <p>We take your case on a contingency basis, which means you pay nothing unless we win.</p>
  </div>
  <div class="abs hex s-hex" style="left:258px;top:180px"><svg width="30" height="34" viewBox="0 0 24 24" fill="#fff"><circle cx="9" cy="4" r="2.3"/><path d="M6 8h6v7h-1.5v7h-3v-7H6z"/><path d="M15 10h6v12h-6z" opacity=".85"/></svg></div>
  <div class="abs hex s-hex" style="left:599px;top:154px"><svg width="34" height="34" viewBox="0 0 24 24" fill="none" stroke="#fff" stroke-width="1.6"><path d="M12 3v18M5 21h14M4 7h16M7 7l-3 7h6zM17 7l-3 7h6z"/></svg></div>
  <div class="abs hex s-hex" style="left:941px;top:180px"><svg width="30" height="30" viewBox="0 0 24 24" fill="none" stroke="#fff" stroke-width="2"><circle cx="12" cy="12" r="9"/><path d="M5.6 5.6l12.8 12.8"/></svg></div>
</section>

<section class="know">
  <div class="abs label center" style="top:108px">Florida Personal Injury Law</div>
  <h2 class="abs h2 center" style="top:134px">What You Need to Know</h2>
  <p class="abs center" style="top:198px;font-size:14px;color:var(--ink)">Your Rights and Legal Protections</p>
  <div class="abs know-photo" role="img" aria-label="Person in a shirt holding a sign reading Comparative Negligence"></div>
  <div class="abs know-card">
    <h3>Comparative Negligence<br><span>(Florida Statutes §768.81)</span></h3>
    <p>Even if you were partially at fault, you can still recover compensation. Your damages will be reduced based on your percentage of fault.</p>
    <div style="margin-top:30px">
      <span class="arrow" style="background:var(--gold)"><svg width="12" height="12" viewBox="0 0 12 12"><path d="M8 1L3 6l5 5" stroke="#fff" stroke-width="2" fill="none"/></svg></span><span class="arrow" style="background:var(--ink)"><svg width="12" height="12" viewBox="0 0 12 12"><path d="M4 1l5 5-5 5" stroke="#fff" stroke-width="2" fill="none"/></svg></span>
    </div>
  </div>
</section>

<section class="promise">
  <div class="abs label center" style="top:50px;color:var(--white)">The Darrow Law Firm</div>
  <h2 class="abs h2 center" style="top:80px;color:#f6eadb">Where Justice Meets Dedication</h2>
  <div class="abs promise-item" style="left:160px">
    <svg class="hex-o" viewBox="0 0 80 88"><polygon points="40,3 77,23 77,65 40,85 3,65 3,23" fill="none" stroke="#fff" stroke-width="3"/><circle cx="32" cy="40" r="7" fill="#fff"/><circle cx="48" cy="40" r="7" fill="#fff"/><path d="M20 62a12 12 0 0124 0zM36 62a12 12 0 0124 0z" fill="#fff"/></svg>
    <div>Free<br>Consultation</div>
  </div>
  <div class="abs promise-item" style="left:472px">
    <svg class="hex-o" viewBox="0 0 80 88"><polygon points="40,3 77,23 77,65 40,85 3,65 3,23" fill="none" stroke="#fff" stroke-width="3"/><text x="40" y="42" text-anchor="middle" font-family="Montserrat,sans-serif" font-weight="700" font-size="14" fill="#fff">NO</text><rect x="20" y="48" width="40" height="18" fill="#fff"/><text x="40" y="62" text-anchor="middle" font-family="Montserrat,sans-serif" font-weight="700" font-size="13" fill="#c4935c">FEES</text></svg>
    <div>No Fees<br>Unless We Win</div>
  </div>
  <div class="abs promise-item" style="left:785px">
    <svg class="hex-o" viewBox="0 0 80 88"><polygon points="40,3 77,23 77,65 40,85 3,65 3,23" fill="none" stroke="#fff" stroke-width="3"/><circle cx="40" cy="34" r="8" fill="#fff"/><path d="M26 64c0-10 6-16 14-16s14 6 14 16z" fill="#fff"/></svg>
    <div>Aggressive<br>Representation</div>
  </div>
</section>

<section class="cta">
  <div class="abs cta-photo" role="img" aria-label="Attorney in a navy suit with a red tie"></div>
  <h2 class="abs" style="left:545px;top:112px;width:560px">Take the First Step Toward Justice</h2>
  <p class="abs" style="left:545px;top:193px;font-size:14px;color:var(--ink)">Let Us Fight for the Compensation You Deserve</p>
  <p class="abs" style="left:545px;top:220px;width:540px;font-size:14px;line-height:25px;color:var(--ink)">If you have been injured due to someone else’s negligence, do not wait. Time-sensitive deadlines could impact your case.</p>
  <div class="abs pill light" style="left:545px;top:286px;width:232px;height:50px">
    <div class="sq" style="height:46px"><svg width="22" height="22" viewBox="0 0 24 24" fill="#fff"><path d="M6.6 10.8a15 15 0 006.6 6.6l2.2-2.2c.3-.3.7-.4 1-.2 1.1.4 2.3.6 3.6.6.6 0 1 .4 1 1V20c0 .6-.4 1-1 1A17 17 0 013 4c0-.6.4-1 1-1h3.5c.6 0 1 .4 1 1 0 1.3.2 2.5.6 3.6.1.3 0 .7-.2 1z"/></svg></div>
    <div><b>Free Consultation :</b>(305) 555-0182</div>
  </div>
  <div class="abs pill light" style="left:793px;top:286px;width:285px;height:50px">
    <div class="sq" style="height:46px"><svg width="22" height="22" viewBox="0 0 24 24" fill="#fff"><path d="M2 5h20v14H2V5zm2 2v.5l8 5 8-5V7H4z"/></svg></div>
    <div><b>Email:</b>info@darrowlegal-example.com</div>
  </div>
</section>

<footer class="site-footer">
  <nav class="abs foot-nav">
    <a>Home</a><span>|</span><a>About Us</a><span>|</span><a>Why Choose The Darrow</a><span>|</span><a>Why Choose The Darrow</a><span>|</span><a>Our Strategy</a><span>|</span><a>Practice Areas</a><span>|</span><a>What You Need to Know</a><span>|</span><a>Contact</a>
  </nav>
  <div class="abs" style="left:111px;top:122px;width:225px;text-align:center">
    <div style="width:50px;height:50px;border:2px solid var(--white);margin:0 auto 8px"></div>
    <div style="font-size:44px;font-weight:600;line-height:48px">Darrow</div>
    <div style="font-size:14px;font-weight:600;letter-spacing:5px">LAW FIRM</div>
  </div>
  <div class="abs foot-col" style="left:365px">
    <div class="circle" style="width:46px;height:46px;flex:none"><svg width="20" height="20" viewBox="0 0 24 24" fill="#fff"><path d="M12 2a7 7 0 00-7 7c0 5 7 13 7 13s7-8 7-13a7 7 0 00-7-7zm0 9.5A2.5 2.5 0 1112 6.5a2.5 2.5 0 010 5z"/></svg></div>
    <div><b>LOCATION :</b>410 Merrick Way, Coral<br>Gables, FL 33134</div>
  </div>
  <div class="abs foot-col" style="left:631px">
    <div class="circle" style="width:46px;height:46px;flex:none"><svg width="20" height="20" viewBox="0 0 24 24" fill="#fff"><path d="M6.6 10.8a15 15 0 006.6 6.6l2.2-2.2c.3-.3.7-.4 1-.2 1.1.4 2.3.6 3.6.6.6 0 1 .4 1 1V20c0 .6-.4 1-1 1A17 17 0 013 4c0-.6.4-1 1-1h3.5c.6 0 1 .4 1 1 0 1.3.2 2.5.6 3.6.1.3 0 .7-.2 1z"/></svg></div>
    <div><b>PHONE NUMBER :</b>(305) 555-0182</div>
  </div>
  <div class="abs foot-col" style="left:861px">
    <div class="circle" style="width:46px;height:46px;flex:none"><svg width="20" height="20" viewBox="0 0 24 24" fill="#fff"><path d="M2 5h20v14H2V5zm2 2v.5l8 5 8-5V7H4z"/></svg></div>
    <div><b>EMAIL US :</b>info@darrowlegal-example.com</div>
  </div>
  <div class="abs" style="left:396px;top:246px;width:700px;height:1px;background:#555"></div>
  <div class="abs copy">© 2025 Darrow Law Firm | All rights reserved.</div>
  <div class="abs circle" style="left:996px;top:258px;width:26px;height:26px"></div>
  <div class="abs circle" style="left:1027px;top:258px;width:26px;height:26px"></div>
  <div class="abs circle" style="left:1058px;top:258px;width:26px;height:26px"></div>
</footer>

</body>
</html>
```